brovalux business card

We are a commercial cleaning/janitorial service company our main target is building owners and managers.
Would like to see the icon as a background shadow in the front and the full logo in white on the back with a blue background.  On the card:
Dorn Pevsky, Operations Manager, dorn@brovalux-example.com
47215-K Harlow Ave. 9 #382
Pinecrest, IN 47912
555.604.2817, 888.555.4163

Updates
please include cell 555.318.6247
                                   
Thank you
If possible the fading logo on the front should be very subtle and light and lets look at centering that as well
thanks

```html
<!DOCTYPE html>
<html lang="en">
<head>
<meta charset="utf-8">
<title>brovalux business card</title>
<link href="https://fonts.googleapis.com/css2?family=Source+Sans+3:wght@400;600&display=swap" rel="stylesheet">
<style>
  :root {
    --stage: #2e2e2e;
    --navy-deep: #0d2a55;
    --navy-mid: #1f4f8c;
    --navy-light: #4a86c2;
    --card-white: #ffffff;
    --card-grey: #d9d9d9;
    --ink: #2a2a2a;
    --brand-blue: #1f5ba8;
    --white: #ffffff;
    --shadow-mark-dark: rgba(255, 255, 255, 0.07);
    --shadow-mark-light: rgba(0, 0, 0, 0.035);
  }
  * { margin: 0; padding: 0; box-sizing: border-box; }
  html, body {
    width: 1200px; height: 900px; overflow: hidden;
    background: var(--stage);
    font-family: "Source Sans 3", "Myriad Pro", Arial, sans-serif;
  }
  .canvas { position: relative; width: 1200px; height: 900px; }

  .card { position: absolute; width: 570px; height: 322px; overflow: hidden; }

  .background-mark {
    position: absolute; border-radius: 50%;
    width: 300px; height: 300px; left: 50%; top: 50%;
    transform: translate(-50%, -50%);
  }

  /* Back of card: blue with white wordmark */
  .card-back {
    left: 100px; top: 138px;
    background: radial-gradient(ellipse 70% 90% at 62% 20%, var(--navy-light) 0%, var(--navy-mid) 40%, var(--navy-deep) 100%);
  }
  .card-back .background-mark { background: var(--shadow-mark-dark); }
  .card-back .brand {
    position: absolute; left: 100px; top: 110px;
    display: flex; align-items: center; gap: 18px;
  }
  .brand-dot { width: 86px; height: 86px; border-radius: 50%; background: var(--white); flex: none; }
  .card-back .brand-name {
    font-size: 62px; font-weight: 600; color: var(--white);
    line-height: 1; letter-spacing: 0.5px;
  }
  .card-back .tagline {
    position: absolute; left: 212px; top: 176px;
    font-size: 17px; font-weight: 600; color: var(--white); letter-spacing: 2px;
  }
  .card-back .website {
    position: absolute; left: 0; right: 0; top: 248px; text-align: center;
    font-size: 19px; color: var(--white);
  }

  /* Front of card: white with details */
  .card-front {
    left: 510px; top: 428px; height: 320px;
    background: radial-gradient(ellipse 80% 100% at 60% 35%, var(--card-white) 0%, #f3f3f3 55%, var(--card-grey) 100%);
  }
  .card-front .background-mark { background: var(--shadow-mark-light); }
  .card-front .brand {
    position: absolute; left: 306px; top: 62px;
    display: flex; align-items: center; gap: 12px;
  }
  .card-front .brand-dot { width: 46px; height: 46px; background: var(--brand-blue); }
  .card-front .brand-name {
    font-size: 36px; font-weight: 600; color: var(--brand-blue); line-height: 1;
  }
  .card-front .tagline {
    position: absolute; left: 366px; top: 96px;
    font-size: 11px; font-weight: 600; color: var(--ink); letter-spacing: 1.4px;
  }
  .person {
    position: absolute; right: 306px; top: 172px; text-align: right; color: var(--ink);
  }
  .person-name { font-size: 19px; line-height: 24px; }
  .person-role { font-size: 13px; line-height: 20px; }
  .person-email { font-size: 15px; line-height: 20px; }
  .contact {
    position: absolute; left: 305px; top: 172px; color: var(--ink);
    font-size: 17px; line-height: 23px;
  }
  .contact .address { margin-top: 16px; }
</style>
</head>
<body>
<main class="canvas">
  <section class="card card-back" aria-label="Card back">
    <span class="background-mark" aria-hidden="true"></span>
    <div class="brand">
      <span class="brand-dot"></span>
      <span class="brand-name">brovalux</span>
    </div>
    <p class="tagline">Building Services</p>
    <p class="website">www.brovalux-example.com</p>
  </section>

  <section class="card card-front" aria-label="Card front">
    <span class="background-mark" aria-hidden="true"></span>
    <div class="brand">
      <span class="brand-dot"></span>
      <span class="brand-name">brovalux</span>
    </div>
    <p class="tagline">Building Services</p>
    <div class="person">
      <p class="person-name">Dorn Pevsky</p>
      <p class="person-role">Operations Manager</p>
      <p class="person-email">dorn@brovalux-example.com</p>
    </div>
    <div class="contact">
      <p>Cell 555.318.6247</p>
      <p>Office 555.604.2817</p>
      <p>Direct 888.555.4163</p>
      <div class="address">
        <p>47215-K Harlow Ave. 9 #382</p>
        <p>Pinecrest, IN 47912</p>
      </div>
    </div>
  </section>
</main>
</body>
</html>
```